Designer sehr zu empfehlen, engagiert und unermüdlich auf Wünsche eingehend. Gerne wieder.
Zielgruppe
Ich berate im Bereich der Telemedizin. Zielgruppe sind Ärzte, Krankenkassen, Politiker.
Aufgabenstellung
Auf der Visitenkarte sollen Adresse, e-mail, Handynummer vorhanden sein.
Briefpapier bitte im Pages-Format.

```html
<!DOCTYPE html>
<html lang="de">
<head>
<meta charset="utf-8">
<title>telvana Briefpapier – Vorder- und Rückseite</title>
<link href="https://fonts.googleapis.com/css2?family=Oxanium:wght@400;600&family=Jura:wght@400;600;700&display=swap" rel="stylesheet">
<style>
  :root {
    --green: #97c11f;
    --ink: #1a1a1a;
    --grey: #6d6e70;
    --paper: #ffffff;
    --stage: #ffffff;
    --sig-tint: #dfe7f3;
  }
  * { margin: 0; padding: 0; box-sizing: border-box; }
  html, body { width: 1200px; height: 848px; overflow: hidden; background: var(--stage); }
  body { position: relative; font-family: "Jura", sans-serif; color: var(--ink); }

  .side-title {
    position: absolute; top: 40px;
    font-family: "Oxanium", sans-serif; font-weight: 400;
    font-size: 46px; letter-spacing: -0.5px; color: #111;
  }
  .side-title--front { left: 49px; }
  .side-title--back { left: 661px; }

  .sheet {
    position: absolute; top: 108px; width: 488px; height: 691px;
    box-shadow: 0 0 3px rgba(0,0,0,0.18);
  }
  .sheet--front { left: 51px; background: var(--paper); }
  .sheet--back { left: 663px; background: var(--green); }

  .edge-band { position: absolute; right: 0; top: 0; width: 14px; height: 100%; background: var(--green); }

  .brand { position: absolute; left: 0; width: 474px; top: 20px; text-align: center; }
  .brand__name { font-family: "Jura", sans-serif; font-weight: 600; font-size: 44px; color: var(--grey); line-height: 1; }
  .brand__tag { font-size: 12px; letter-spacing: 6px; color: #333; margin-top: 0; padding-left: 60px; }

  .sender-line { position: absolute; left: 46px; top: 110px; font-size: 6px; font-weight: 600; }
  .sender-line .mark { color: var(--green); font-weight: 700; }

  .recipient { position: absolute; left: 46px; top: 121px; font-size: 8.6px; line-height: 8.4px; font-weight: 600; font-style: normal; }
  .recipient .city { margin-top: 8px; }

  .reference { position: absolute; left: 291px; top: 120px; font-size: 8.6px; line-height: 11.5px; font-weight: 600; }
  .reference dl { display: grid; grid-template-columns: 75px auto; }
  .reference .gap { margin-top: 6px; }

  .date { position: absolute; right: 34px; top: 212px; font-size: 8.6px; font-weight: 600; }

  .fold-mark { position: absolute; left: 0; height: 0; border-top: 0.6px solid #777; }
  .fold-mark--1 { top: 244px; width: 17px; }
  .fold-mark--2 { top: 345px; width: 11px; }
  .fold-mark--3 { top: 488px; width: 17px; }

  .letter { position: absolute; left: 58px; top: 242px; width: 386px; font-size: 8.5px; line-height: 10px; font-weight: 600; }
  .letter p { margin-bottom: 9.6px; }
  .letter .subject { font-weight: 700; }
  .letter .closing { margin-top: 19px; margin-bottom: 0; }
  .signature { width: 74px; height: 34px; background: var(--sig-tint); margin: 1px 0 0 2px; }
  .signer { line-height: 10px; }
  .signer strong { font-weight: 700; }

  .footer-rule { position: absolute; left: 46px; top: 641px; width: 396px; height: 1px; background: var(--green); }
  .footer { position: absolute; left: 46px; top: 647px; width: 396px; display: grid; grid-template-columns: 103px 103px 103px 87px; font-size: 6.6px; line-height: 7.4px; color: var(--grey); font-weight: 600; }
  .footer .accent { color: var(--green); }
  .footer .web { text-align: right; display: block; }

  .badge {
    position: absolute; left: 138px; top: 228px; width: 212px; height: 212px;
    border-radius: 50%; background: var(--paper);
    display: flex; align-items: center; justify-content: center;
  }
  .badge__name { font-family: "Jura", sans-serif; font-weight: 600; font-size: 40px; color: var(--grey); }
  .back-url { position: absolute; left: 0; width: 100%; top: 645px; text-align: center; font-family: "Oxanium", sans-serif; font-weight: 600; font-size: 17px; color: var(--paper); }
</style>
</head>
<body>
  <h1 class="side-title side-title--front">Vorderseite.</h1>
  <h1 class="side-title side-title--back">Rückseite.</h1>

  <section class="sheet sheet--front" aria-label="Briefbogen Vorderseite">
    <div class="edge-band"></div>

    <header class="brand">
      <div class="brand__name">telvana</div>
      <div class="brand__tag">Telemedizin</div>
    </header>

    <div class="sender-line"><span class="mark">telvana</span> · Lindenweg 14 · 24103 Kiel</div>

    <address class="recipient">
      <div>Paul Beispiel</div>
      <div>Hafenstraße 9</div>
      <div class="city">23552 Lübeck</div>
    </address>

    <div class="reference">
      <dl><dt>Unser Zeichen:</dt><dd>2735-HF</dd></dl>
      <dl class="gap"><dt>Ansprechpartner:</dt><dd>Jana Berger</dd>
        <dt>Telefon:</dt><dd>0 45 61 / 78 90 12</dd>
        <dt>E-Mail:</dt><dd>berger@telvana.de</dd></dl>
    </div>

    <div class="date">Datum: 31.03.2014</div>

    <span class="fold-mark fold-mark--1"></span>
    <span class="fold-mark fold-mark--2"></span>
    <span class="fold-mark fold-mark--3"></span>

    <article class="letter">
      <p class="subject">Dies ist ein Blindbetreff!</p>
      <p>Sehr geehrter Herr Beispiel,</p>
      <p>Lorem ipsum dolor sit amet, consetetur sadipscing elitr, sed diam nonumy eirmod tempor ut. labore et dolore magna aliquyam erat, sed diam voluptua. At vero eos et accusam et justo duo dolores et ea rebum. Stet clita kasd gubergren, no sea takimata sanctus est Lorem ipsum dolor sit amet. Lorem ipsum dolor sit amet, consetetur sadipscing elitr, sed diam nonumy eirmod tempor invidunt ut labore et dolore magna aliquyam erat, sed diam voluptua.</p>
      <p>Stet clita kasd gubergren, no sea takimata sanctus est Lorem ipsum dolor sit amet. Lorem ipsum dolor sit amet, consetetur sadipscing elitr, sed diam nonumy eirmod tempor invidunt ut labore et dolore magna aliquyam erat, sed diam voluptua. Vero eos et accusam et justo duo dolores et ea. Stet clita kasd gubergren, no sea takimata sanctus est Lorem ipsum dolor sit amet.</p>
      <p>Duis autem vel eum iriure dolor in hendrerit in vulputate velit esse molestie consequat, vel illum dolore eu feugiat nulla facilisis at vero eros et accumsan et iusto odio dignissim qui blandit praesent luptatum zzril delenit augue duis dolore te feugait nulla facilisi.</p>
      <p>Bei Rückfragen stehe ich Ihnen gerne zur Verfügung.</p>
      <p class="closing">Mit freundlichen Grüßen</p>
      <div class="signature" role="img" aria-label="Handschriftliche Unterschrift"></div>
      <div class="signer"><strong>Jana Berger</strong><br>Office-Manager</div>
    </article>

    <div class="footer-rule"></div>
    <footer class="footer">
      <div><span class="accent">telvana</span> Telemedizin GmbH<br>Lindenweg 14<br>24103 Kiel</div>
      <div>Tel&nbsp; 0 45 61 / 78 90 10<br>Fax 0 45 61 / 78 90 19<br>Mail info@telvana.de</div>
      <div>Amtsgericht Kiel<br>HRB&nbsp;&nbsp;&nbsp;&nbsp;&nbsp;&nbsp; 48213<br>USt-ID-Nr. DE9876543210</div>
      <div>Geschäftsführung: Jonas Kern &amp; Ute Weiland<span class="accent web">telvana.de</span></div>
    </footer>
  </section>

  <section class="sheet sheet--back" aria-label="Briefbogen Rückseite">
    <div class="badge"><span class="badge__name">telvana</span></div>
    <div class="back-url">telvana.de</div>
  </section>
</body>
</html>
```